WE RISE UP - Personal Growth Seminar

The project is collaboration between Desmond Pellow and Marisa Dunford. It will combine the skills of both parties to launch an inspirational and motivation Personal Growth Seminar. We are looking for an e-flyer and a general design that we can use in our promotional work

The programme is a one day seminar which will show delegates how to

1) Kick start your life
2) Overcome obstacles and self sabotage
3) Take control of your future
4) Think bigger than you thought possible
5) Increase your confidence and self belief
6) Six steps to WE RISE UP success

Our values for the seminar, that the eflyer should represent are:
Professional
Freedom
Nature (really important theme)
Fun
Honest
Balance
Integrity

We want to GRAB people's attention and then ENGAGE them into booking onto the seminar. We will send over details for the links to the seminar and phone numbers etc later, so they need to be incorporated. The seminar will be held in a hotel called The Brackenhall (nature and growth theme)

The one thing to remember is, to step back from the design and ask yourself would you book the seminar, based on what you see.

Our websites so you can see our current themes are www.marisadunford.com and www.desmondpellow.co.uk

Target Market(s)

Adults based in UK, between 25 and 50 years of age.

Industry/Entity Type

Hotel

Requirements
Must have
• Nature theme - growth
Fun but professional

Colours green but more vibrant like grass colour, nothing dull or washed out

Nice to have
• The picture will give you an idea but doesn't need to be used, it is just for guidance.

A Tree theme could be used - perhaps with the WE RISE UP on the branches
Should not have
• Should not include cartoons

Gawdy colours or too much text

```html
<!DOCTYPE html>
<html lang="en">
<head>
<meta charset="utf-8">
<title>We Rise Up – One Day Seminar</title>
<link rel="stylesheet" href="https://fonts.googleapis.com/css2?family=Nunito:wght@800;900&family=Righteous&family=Arimo:wght@400;700&display=swap">
<style>
  :root {
    --grass: #2f9e1c;
    --grass-deep: #1f7a10;
    --grass-light: #7fd34a;
    --grass-glow: #b8ef7a;
    --paper: #ffffff;
    --ink: #1d1d1d;
    --ink-soft: #333333;
    --title-white: #f5f5f5;
    --title-shade: #9a9a9a;
  }
  html, body {
    margin: 0;
    padding: 0;
    width: 849px;
    height: 1200px;
    overflow: hidden;
    background: var(--paper);
  }
  .flyer {
    position: relative;
    width: 849px;
    height: 1200px;
    overflow: hidden;
    background: var(--grass);
    font-family: "Arimo", Arial, sans-serif;
    color: var(--paper);
  }
  .flyer p { margin: 0; }
  .layer {
    position: absolute;
    left: 0;
    top: 0;
  }
  .headline {
    position: absolute;
    left: 0;
    width: 849px;
    margin: 0;
    text-align: center;
    font-family: "Nunito", "Arial Rounded MT Bold", sans-serif;
    font-weight: 900;
    line-height: 1;
    white-space: nowrap;
    color: var(--title-white);
    transform-origin: 50% 0;
  }
  .headline-main {
    top: -8px;
    font-size: 146px;
    letter-spacing: -3px;
    transform: scaleY(1.55);
    text-shadow: 0 2px 0 #c9c9c9, 0 4px 0 var(--title-shade), 0 7px 10px rgba(0, 0, 0, 0.45);
  }
  .headline-sub {
    top: 174px;
    font-size: 100px;
    font-weight: 800;
    letter-spacing: -1px;
    transform: scaleY(1.15);
    text-shadow: 0 3px 0 var(--title-shade), 0 7px 10px rgba(0, 0, 0, 0.4);
  }
  .intro {
    position: absolute;
    left: 46px;
    top: 466px;
    width: 520px;
    font-size: 39px;
    line-height: 44px;
    color: var(--paper);
    text-shadow: 1px 2px 2px rgba(0, 0, 0, 0.55);
  }
  .benefits {
    position: absolute;
    left: 46px;
    top: 614px;
    margin: 0;
    padding: 0;
    list-style: none;
    font-weight: 700;
    font-size: 19px;
  }
  .benefits li {
    height: 40.5px;
    line-height: 40.5px;
    white-space: nowrap;
  }
  .benefits li::before {
    content: "•";
    margin-right: 12px;
  }
  .brand-mark {
    font-family: "Righteous", "Arial Black", sans-serif;
    font-size: 27px;
    line-height: 1;
    letter-spacing: 1px;
  }
  .venue-line {
    position: absolute;
    left: 46px;
    white-space: nowrap;
    font-weight: 700;
  }
  .venue-intro { top: 878px; font-size: 21px; }
  .venue-name {
    top: 912px;
    font-family: "Righteous", "Arial Black", sans-serif;
    font-weight: 400;
    font-size: 46px;
    line-height: 1;
    letter-spacing: 0.5px;
  }
  .venue-address { top: 978px; font-size: 15px; }
  .venue-date { top: 1004px; font-size: 22px; }
  .speaker {
    position: absolute;
    width: 200px;
    color: var(--ink);
  }
  .speaker-name {
    font-weight: 700;
    font-size: 20.5px;
    line-height: 24px;
    color: var(--ink-soft);
  }
  .speaker-role {
    margin-top: 2px !important;
    font-size: 17.5px;
    line-height: 24.5px;
    color: var(--ink);
  }
  .speaker-desmond { left: 589px; top: 554px; }
  .speaker-marisa { left: 653px; top: 851px; }
  .websites {
    position: absolute;
    left: 0;
    top: 1106px;
    width: 849px;
    text-align: center;
    font-weight: 700;
    font-size: 29px;
    line-height: 38px;
    text-shadow: 1px 2px 3px rgba(0, 0, 0, 0.7);
  }
</style>
</head>
<body>
<main class="flyer">

  <svg class="layer backdrop" width="849" height="1200" viewBox="0 0 849 1200" aria-hidden="true">
    <rect width="849" height="1200" fill="var(--grass)"/>
    <path class="speaker-panel" d="M849 352 C760 356 650 372 604 425 C566 470 568 560 585 630 C600 700 625 780 640 850 C652 910 650 970 640 1030 L849 1030 Z" fill="var(--paper)"/>
  </svg>

  <svg class="layer grass-header" width="849" height="440" viewBox="0 0 849 440" role="img" aria-label="Close-up photograph of fresh green grass blades with dew drops and soft light">
    <defs>
      <radialGradient id="headerGlow" cx="0.45" cy="0.25" r="0.8">
        <stop offset="0" stop-color="var(--grass-glow)"/>
        <stop offset="0.45" stop-color="var(--grass-light)"/>
        <stop offset="1" stop-color="var(--grass-deep)"/>
      </radialGradient>
    </defs>
    <path d="M0 0 H849 V350 C760 346 650 362 570 385 C430 425 210 425 0 392 Z" fill="url(#headerGlow)"/>
  </svg>

  <svg class="layer grass-footer" width="849" height="1200" viewBox="0 0 849 1200" role="img" aria-label="Photograph of green grass blades in sunlight along the bottom of the flyer">
    <defs>
      <linearGradient id="footerGlow" x1="0" y1="0" x2="0" y2="1">
        <stop offset="0" stop-color="var(--grass-light)"/>
        <stop offset="0.5" stop-color="#58b830"/>
        <stop offset="1" stop-color="var(--grass-deep)"/>
      </linearGradient>
    </defs>
    <path d="M0 1066 C200 1044 420 1022 600 1014 C700 1010 790 1006 849 1000 V1200 H0 Z" fill="url(#footerGlow)"/>
    <path d="M0 1060 C200 1038 420 1016 600 1008 C700 1004 790 1000 849 994" fill="none" stroke="var(--paper)" stroke-opacity="0.75" stroke-width="4"/>
  </svg>

  <svg class="layer portrait" style="left:641px;top:376px" width="150" height="150" viewBox="0 0 150 150" role="img" aria-label="Portrait photograph of speaker Desmond Pellow">
    <defs>
      <radialGradient id="portraitDesmond" cx="0.5" cy="0.4" r="0.6">
        <stop offset="0" stop-color="#c99a7a"/>
        <stop offset="1" stop-color="#3c3a3a"/>
      </radialGradient>
    </defs>
    <circle cx="75" cy="75" r="68" fill="#777" opacity="0.35"/>
    <circle cx="75" cy="72" r="68" fill="#dcdcdc"/>
    <circle cx="75" cy="72" r="62" fill="url(#portraitDesmond)"/>
  </svg>

  <svg class="layer portrait" style="left:618px;top:682px" width="130" height="130" viewBox="0 0 150 150" role="img" aria-label="Portrait photograph of speaker Marisa Dunford">
    <defs>
      <radialGradient id="portraitMarisa" cx="0.5" cy="0.4" r="0.6">
        <stop offset="0" stop-color="#e6c4ad"/>
        <stop offset="1" stop-color="#b9b9b4"/>
      </radialGradient>
    </defs>
    <circle cx="75" cy="75" r="68" fill="#777" opacity="0.35"/>
    <circle cx="75" cy="72" r="68" fill="#dcdcdc"/>
    <circle cx="75" cy="72" r="62" fill="url(#portraitMarisa)"/>
  </svg>

  <h1 class="headline headline-main">We Rise Up</h1>
  <p class="headline headline-sub">one day seminar</p>

  <p class="intro">The programme is a one day seminar which will show delegates how to:-</p>

  <ul class="benefits">
    <li>Kick start your life</li>
    <li>Overcome obstacles and self sabotage</li>
    <li>Take control of your future</li>
    <li>Think bigger than you thought possible</li>
    <li>Increase your confidence and self belief</li>
    <li>Six steps to <span class="brand-mark">WE RISE UP</span> success</li>
  </ul>

  <section class="venue">
    <p class="venue-line venue-intro">The Seminar is to be held at</p>
    <p class="venue-line venue-name">The Brackenhall Hotel</p>
    <p class="venue-line venue-address">First line of the Address • Street Name • Area • Post code</p>
    <p class="venue-line venue-date">On Saturday • 00th • Month • 2011</p>
  </section>

  <section class="speaker speaker-desmond">
    <p class="speaker-name">Desmond Pellow</p>
    <p class="speaker-role">Motivational speaker,<br>professional speaker,<br>inspirational speaker.</p>
  </section>

  <section class="speaker speaker-marisa">
    <p class="speaker-name">Marisa Dunford</p>
    <p class="speaker-role">Change Speaker,<br>Communication<br>Coach and<br>Hypnotherapist.</p>
  </section>

  <p class="websites">Visit our websites www.marisadunford.com<br>and www.desmondpellow.co.uk</p>

</main>
</body>
</html>
```